BRIM Outreach Partners Business Card Rebrand

Hello Designers! We are looking for help designing our new business card to go in conjunction with our company rebrand. Unfortunately, we have an event mid June that requires we get these printed ASAP (before our new website is launched.) We have a mostly complete Brand Book which I have uploaded to this request for your reference to company information, style, fonts. I've also enclosed our logo file in .eps & .jpg. Attached is a sample business card my boss liked but said was "too simple." I made it in Canva and do not profess to be a designer. NOT FOR DESIGN REFERENCE, ONLY FOR CONTEXT Here is what our old website looks like: https://brimoutreachpartners.com/.

```html
<!DOCTYPE html>
<html lang="en">
<head>
<meta charset="utf-8">
<title>BRIM Outreach Partners – Business Card</title>
<link href="https://fonts.googleapis.com/css2?family=Montserrat:wght@400;500;700&display=swap" rel="stylesheet">
<style>
  :root {
    --page-bg: #8a9fc2;
    --brand-blue: #6bbbe8;
    --ink-black: #121212;
    --paper-white: #ffffff;
  }
  * { margin: 0; padding: 0; box-sizing: border-box; }
  html, body {
    width: 1200px; height: 876px; overflow: hidden;
    background: var(--page-bg);
    font-family: "Montserrat", Arial, sans-serif;
    color: var(--paper-white);
  }
  .stage {
    position: relative; width: 1200px; height: 876px;
    display: flex; justify-content: center; align-items: center; gap: 120px;
  }
  .card {
    position: relative; width: 320px; height: 560px; overflow: hidden;
    box-shadow: 0 14px 30px rgba(20, 30, 60, 0.35);
  }
  .card-shapes { position: absolute; inset: 0; }

  /* Front */
  .front-brand {
    position: absolute; top: 292px; left: 0; width: 100%;
    text-align: center; font-weight: 700; font-size: 13px; letter-spacing: 2px;
  }
  .holder { position: absolute; left: 0; bottom: 62px; width: 100%; text-align: center; }
  .holder-name { font-size: 20px; letter-spacing: 0.5px; text-transform: uppercase; }
  .holder-name strong { font-weight: 700; }
  .holder-name span { font-weight: 400; }
  .holder-title { margin-top: 4px; font-size: 12px; letter-spacing: 1.5px; text-transform: uppercase; }

  /* Back */
  .back-brand {
    position: absolute; top: 104px; left: 116px; width: 170px;
    font-weight: 700; font-size: 15px; line-height: 1.15; letter-spacing: 1px;
    text-transform: uppercase;
  }
  .contact-list {
    position: absolute; top: 268px; left: 48px; right: 48px;
    list-style: none; text-align: center;
  }
  .contact-item { padding: 10px 0 12px; }
  .contact-item + .contact-item { border-top: 1px solid rgba(255,255,255,0.85); }
  .contact-icon { display: block; margin: 0 auto 6px; width: 18px; height: 18px; }
  .contact-text { font-size: 12px; letter-spacing: 0.3px; white-space: nowrap; }
</style>
</head>
<body>
<main class="stage">

  <section class="card card-front" aria-label="Card front">
    <svg class="card-shapes" viewBox="0 0 320 560" aria-hidden="true">
      <rect width="320" height="560" fill="var(--ink-black)"/>
      <polygon points="0,0 320,0 320,170 0,228" fill="var(--brand-blue)"/>
      <circle cx="160" cy="198" r="74" fill="var(--paper-white)"/>
    </svg>
    <p class="front-brand">BRIM OUTREACH PARTNERS</p>
    <div class="holder">
      <p class="holder-name"><strong>Darren</strong> <span>Holt-Meyer</span></p>
      <p class="holder-title">Managing Partner</p>
    </div>
  </section>

  <section class="card card-back" aria-label="Card back">
    <svg class="card-shapes" viewBox="0 0 320 560" aria-hidden="true">
      <rect width="320" height="560" fill="var(--brand-blue)"/>
      <polygon points="0,0 320,0 320,212 0,204" fill="var(--ink-black)"/>
      <circle cx="82" cy="122" r="26" fill="var(--brand-blue)"/>
      <line x1="160" y1="222" x2="160" y2="252" stroke="var(--paper-white)" stroke-width="1.5"/>
    </svg>
    <p class="back-brand">BRIM Outreach Partners</p>
    <ul class="contact-list">
      <li class="contact-item">
        <svg class="contact-icon" viewBox="0 0 24 24" aria-hidden="true"><path fill="#fff" d="M6.6 10.8a15.5 15.5 0 0 0 6.6 6.6l2.2-2.2c.3-.3.7-.4 1-.2 1.1.4 2.3.6 3.6.6.6 0 1 .4 1 1V20c0 .6-.4 1-1 1A17 17 0 0 1 3 4c0-.6.4-1 1-1h3.5c.6 0 1 .4 1 1 0 1.3.2 2.5.6 3.6.1.3 0 .7-.2 1z"/></svg>
        <span class="contact-text">+945-555-0142</span>
      </li>
      <li class="contact-item">
        <svg class="contact-icon" viewBox="0 0 24 24" aria-hidden="true"><path fill="#fff" d="M12 2a7 7 0 0 0-7 7c0 5.2 7 13 7 13s7-7.8 7-13a7 7 0 0 0-7-7zm0 9.5a2.5 2.5 0 1 1 0-5 2.5 2.5 0 0 1 0 5z"/></svg>
        <span class="contact-text">Savannah, GA office (Eastern Time)</span>
      </li>
      <li class="contact-item">
        <svg class="contact-icon" viewBox="0 0 24 24" aria-hidden="true"><path fill="#fff" d="M2 5h20v14H2z"/><path fill="none" stroke="#6bbbe8" stroke-width="1.6" d="M2 5l10 8 10-8"/></svg>
        <span class="contact-text">darren@brimoutreachpartners.com</span>
      </li>
    </ul>
  </section>

</main>
</body>
</html>
```